Kindro - Bringing Warmth and Quality to Senior Living

We are a new company based in Sydney, Australia. We have developed a state-of-the-art app for communication between aged care facilities and families.

Kindro has been developed for facilities to augment the best possible care by providing easy, safe and secure communication for families to stay in touch with their loved ones.
Updates

the website needs to be designed so we can add functionality including multilingual support. display in different languages.we also require enquiry and email/data base function. we want it simple and clean so its responsive. the target audience will be 40+ in age. there will be a video on home page. would like to start with 6 pages/ subjects -homepage -about us -our solution -demonstration page, this will be a page that contains videos of people using our product -customer testimonials -contact us

Target Market(s)

Aged care facilities.
Families (over 40’s age group) who are looking for a facility for their loved ones.

Number of Pages Required

5+ page

Font styles to use
Sans Serif

Colors
faa54b
ffffff
0255a3

Requirements
Must have
• - Our corporate colour is #EE8811.
• - If you're using stock photography, please use brimlo prints photos as we have a license for their photos.
• - The design needs to be responsive (mobile and desktop)
• -White space on each page
Nice to have
• -need to leave a place for a future animation video to be added in on the home tab
Should not have
• we don't want flash technology

```html
<!DOCTYPE html>
<html lang="en">
<head>
<meta charset="utf-8">
<title>Kindro - Bringing Warmth and Quality to Senior Living</title>
<link rel="stylesheet" href="https://fonts.googleapis.com/css2?family=Poppins:wght@300;400;500;600;700&display=swap">
<style>
:root{
  --brand:#ee8811;
  --brand-soft:#faa54b;
  --cta:#ffb400;
  --ink:#13253b;
  --text:#555b63;
  --muted:#9aa0a6;
  --nav:#1f252b;
  --footer:#0d1a2b;
  --line:#e8eaed;
  --white:#ffffff;
}
*{box-sizing:border-box;margin:0;padding:0}
html,body{width:1200px;height:2209px;overflow:hidden;background:var(--white)}
body{position:relative;font-family:'Poppins',sans-serif;color:var(--text)}
.abs{position:absolute}

/* top strip */
.topbar{top:0;left:0;width:1200px;height:31px;border-bottom:1px solid var(--line);font-size:10.5px;font-weight:300;color:#555}
.topbar b{font-weight:600;color:#111}
.topbar .item{position:absolute;top:8px;white-space:nowrap}
.topbar .sep{position:absolute;top:7px;width:1px;height:16px;background:var(--line)}

/* header */
.header{top:31px;left:0;width:1200px;height:63px}
.brand{display:flex;align-items:center;gap:8px;font-weight:600;color:var(--brand)}
.brand .dot{width:26px;height:26px;border-radius:50%;border:3px solid var(--brand)}
.hotline{left:632px;top:15px;line-height:1.25}
.hotline small{display:block;font-size:11.5px;color:var(--brand);font-weight:500}
.hotline strong{font-size:15px;letter-spacing:2.5px;color:#111;font-weight:600}
.search{left:739px;top:16px;width:288px;height:32px;border:1px solid var(--line);border-radius:16px;background:#fafafa;font-size:11px;color:#999;padding:8px 18px}
.social{width:32px;height:32px;border-radius:50%}

/* nav */
.nav{top:94px;left:0;width:1200px;height:36px;background:var(--nav);font-size:12px;color:var(--white)}
.nav a{position:absolute;top:11px;color:var(--white);text-decoration:none}
.nav a.active{color:var(--brand)}
.nav .bar{position:absolute;top:8px;width:1px;height:20px;background:#3b434b}
.nav .active-line{position:absolute;left:14px;top:33px;width:81px;height:3px;background:var(--brand)}
.nav .tag{position:absolute;right:30px;top:11px;color:var(--brand);font-size:11.5px}

/* hero */
.hero{top:130px;left:0;width:1200px;height:594px;background:linear-gradient(120deg,#c9ccd6 0%,#9da7ba 40%,#7e8aa3 70%,#545c6b 100%)}

/* story */
.photo{border-radius:50%}
.ring{border-radius:50%;border:1.5px dashed #cfd3d8}
.badge{width:50px;height:50px;border-radius:50%;background:var(--brand);color:var(--white);font-size:27px;font-weight:400;display:flex;align-items:center;justify-content:center}
.story h2{font-size:21px;font-weight:600;color:var(--ink);letter-spacing:.2px}
.story p{font-size:12px;line-height:21px;font-weight:300;color:#444}

/* contact */
.contact-title{left:0;width:1200px;text-align:center;top:1500px;font-size:34px;font-weight:600;color:var(--ink)}
.contact-sub{left:0;width:1200px;text-align:center;top:1549px;font-size:12px;font-weight:300;color:#555}
.card{left:149px;top:1603px;width:648px;height:349px;background:var(--white);box-shadow:0 2px 14px rgba(0,0,0,.08)}
.card h3{position:absolute;left:29px;top:21px;font-size:22px;font-weight:600;color:var(--ink)}
.card .lead{position:absolute;left:29px;top:52px;font-size:11.5px;font-weight:300;color:#555}
.field{position:absolute;border:1px solid #eceef0;border-radius:20px;font-size:9px;letter-spacing:.8px;color:#888;display:flex;align-items:center;gap:10px;padding-left:18px}
.field.filled{font-size:12.5px;letter-spacing:0;color:#222}
.field.area{border-radius:14px;align-items:flex-start;padding-top:18px}
.btn{position:absolute;left:30px;top:272px;width:154px;height:40px;background:var(--cta);color:var(--white);font-size:9.5px;letter-spacing:1px;display:flex;align-items:center;justify-content:center;box-shadow:0 8px 14px rgba(255,180,0,.35)}
.info{left:829px;display:flex;gap:12px;align-items:center}
.info .ico{width:38px;height:38px;border-radius:50%;background:var(--cta);display:flex;align-items:center;justify-content:center}
.info strong{display:block;font-size:14px;font-weight:500;color:#333}
.info span{display:block;font-size:12px;color:#444}

/* footer */
.footer{left:0;top:2018px;width:1200px;height:191px;background:var(--footer)}
.footer .brand{position:absolute;left:153px;top:57px;font-size:28px}
.footer nav a{position:absolute;top:79px;font-size:12px;color:#d5d9de;text-decoration:none}
.footer .under{position:absolute;left:368px;top:123px;width:33px;height:2px;background:var(--brand)}
.footer .rule{position:absolute;left:153px;top:126px;width:893px;height:1px;background:#243247}
.footer .fsoc{position:absolute;top:67px;width:26px;height:26px;border-radius:50%;background:var(--white)}
.footer .copy{position:absolute;left:153px;top:153px;font-size:11px;color:#3d4b5e}
.footer .back{position:absolute;left:973px;top:153px;font-size:11px;color:#3d4b5e;display:flex;gap:12px;align-items:center}
</style>
</head>
<body>

<div class="abs topbar">
  <div class="item" style="left:36px"><b>Contact</b> - To learn more about the Kindro solution, phone - 9170 2284</div>
  <div class="sep" style="left:424px"></div>
  <div class="item" style="left:504px"><b>Email</b> - hello@kindro.co</div>
  <div class="sep" style="left:655px"></div>
  <div class="item" style="left:708px"><b>Carers</b> - Ability to access a simple method of quality care</div>
  <div class="sep" style="left:1046px"></div>
  <div class="item" style="left:1092px;display:flex;align-items:center;gap:6px">
    <svg width="14" height="14" viewBox="0 0 14 14"><circle cx="7" cy="7" r="6.5" fill="#2a4fa0"/><path d="M1 7h12M7 1v12" stroke="#fff" stroke-width="3"/><path d="M1 7h12M7 1v12" stroke="#d22" stroke-width="1.4"/></svg>
    <span style="color:#888">English ⌄</span>
  </div>
</div>

<header class="abs header">
  <div class="abs brand" style="left:38px;top:16px;font-size:28px"><span class="dot"></span>Kindro</div>
  <svg class="abs" style="left:590px;top:17px" width="32" height="32" viewBox="0 0 32 32"><path d="M8 4c2 0 4 5 4 6s-3 2-3 3c1 4 5 8 9 9 1 0 2-3 3-3s6 2 6 4-3 5-5 5C12 28 4 20 4 9c0-2 2-5 4-5z" fill="none" stroke="#ee8811" stroke-width="1.6"/><path d="M19 6a8 8 0 0 1 7 7M19 2a12 12 0 0 1 11 11" fill="none" stroke="#ee8811" stroke-width="1.6"/></svg>
  <div class="abs hotline"><small>Kindro Contact</small><strong>9170 2284</strong></div>
  <div class="abs search">Search...
    <svg style="position:absolute;right:14px;top:8px" width="16" height="16" viewBox="0 0 16 16"><circle cx="7" cy="7" r="5.5" fill="none" stroke="#c0267a" stroke-width="1.8"/><path d="M11 11l4 4" stroke="#c0267a" stroke-width="1.8"/></svg>
  </div>
  <div class="abs social" style="left:1049px;top:16px;background:#3b5998"></div>
  <div class="abs social" style="left:1090px;top:16px;background:#1da1f2"></div>
  <div class="abs social" style="left:1130px;top:16px;background:var(--brand)"></div>
</header>

<nav class="abs nav">
  <a class="active" style="left:36px">Home</a>
  <span class="bar" style="left:95px"></span>
  <a style="left:120px">About us</a>
  <span class="bar" style="left:195px"></span>
  <a style="left:219px">Our Solution</a>
  <span class="bar" style="left:312px"></span>
  <a style="left:337px">Demonstration</a>
  <span class="bar" style="left:446px"></span>
  <a style="left:471px">Customer Testimonials</a>
  <span class="bar" style="left:626px"></span>
  <a style="left:650px">Contact Us</a>
  <span class="active-line"></span>
  <span class="tag">Easier communication between residents and families</span>
</nav>

<section class="abs hero" role="img" aria-label="Video still: senior couple chatting with a care advisor over coffee">
  <svg class="abs" style="left:558px;top:255px" width="84" height="84" viewBox="0 0 84 84"><circle cx="42" cy="42" r="42" fill="#ee8811"/><path d="M32 24l28 18-28 18z" fill="#fff"/></svg>
</section>

<section class="story">
  <svg class="abs" style="left:0;top:980px" width="1200" height="360" viewBox="0 980 1200 360">
    <path d="M560 994V1100q0 14 14 14h68q14 0 14 14V1300q0 22 32 22" fill="none" stroke="#cfd3d8" stroke-width="1.3" stroke-dasharray="3 3"/>
    <circle cx="560" cy="994" r="5" fill="#c9cdd2"/>
    <circle cx="688" cy="1322" r="5" fill="#c9cdd2"/>
  </svg>

  <div class="abs ring" style="left:267px;top:794px;width:300px;height:300px"></div>
  <div class="abs photo" role="img" aria-label="Photo: smiling woman meeting with an advisor" style="left:280px;top:807px;width:274px;height:274px;background:radial-gradient(circle at 40% 40%,#e6d6bf,#b8b2a8 55%,#4c4c4f)"></div>
  <div class="abs badge" style="left:308px;top:805px">1</div>
  <h2 class="abs" style="left:615px;top:868px">WHAT IS KINDRO</h2>
  <p class="abs" style="left:615px;top:912px;width:400px">Kindro is a state-of-the-art solution that provides communication between aged care facilities, residents and families.<br>Kindro has been developed for facilities to augment the best possible care by providing easy, safe and secure communication for families to stay in touch with their loved ones.</p>

  <div class="abs ring" style="left:686px;top:1144px;width:300px;height:300px"></div>
  <div class="abs photo" role="img" aria-label="Photo: three colleagues reviewing documents at a table" style="left:699px;top:1157px;width:274px;height:274px;background:radial-gradient(circle at 55% 45%,#f0ece6,#c9c2b6 55%,#3b3a3c)"></div>
  <div class="abs badge" style="left:882px;top:1135px">2</div>
  <h2 class="abs" style="left:316px;top:1177px;width:300px;text-align:right">WHY KINDRO?</h2>
  <p class="abs" style="left:190px;top:1222px;width:426px;text-align:right">With the spotlight on aged care, facilities need every advantaged to demonstrate excellence to residents and their families, and Kindro provide a solution.Reports have been so confronting within the industry that a Royal Commission into Aged Care Quality and Safety was created by the Federal Government.<br>There has never been a better time for facilities to update the provision of services through the use of technology.<br>Facilities that already provide quality care can enhance and expand that care for facility management, families and residents.</p>
</section>

<h2 class="abs contact-title">Contact Us</h2>
<p class="abs contact-sub">There are many variations of passages of Lorem Ipsum available.</p>

<form class="abs card">
  <h3>Request Call Back.</h3>
  <p class="lead">We are here to answer any qustion you may have</p>
  <svg style="position:absolute;left:564px;top:34px" width="38" height="36" viewBox="0 0 38 36"><path d="M36 2L2 18l12 4 4 12 6-9M36 2L14 22M36 2l-12 23" fill="none" stroke="#9aa0a6" stroke-width="1.1"/></svg>
  <div class="field" style="left:27px;top:91px;width:285px;height:40px">
    <svg width="12" height="12" viewBox="0 0 12 12"><circle cx="6" cy="4" r="2.6" fill="none" stroke="#999"/><path d="M1 12c0-3 2.2-4.5 5-4.5s5 1.5 5 4.5" fill="none" stroke="#999"/></svg>YOUR NAME*</div>
  <div class="field filled" style="left:27px;top:143px;width:285px;height:40px">
    <svg width="14" height="10" viewBox="0 0 14 10"><rect x=".5" y=".5" width="13" height="9" fill="none" stroke="#999"/><path d="M.5 .5l6.5 5 6.5-5" fill="none" stroke="#999"/></svg>hello@kindro.co</div>
  <div class="field" style="left:27px;top:195px;width:285px;height:40px">
    <svg width="9" height="13" viewBox="0 0 9 13"><rect x=".5" y=".5" width="8" height="12" rx="1.5" fill="none" stroke="#999"/></svg>MOBILE NO*</div>
  <div class="field area" style="left:322px;top:91px;width:294px;height:140px">YOUR MESSAGE*</div>
  <div class="btn">SEND MESSAGE</div>
</form>

<div class="abs info" style="top:1689px">
  <div class="ico"><svg width="16" height="12" viewBox="0 0 16 12"><rect x=".5" y=".5" width="15" height="11" fill="none" stroke="#fff"/><path d="M.5 .5l7.5 6 7.5-6" fill="none" stroke="#fff"/></svg></div>
  <div><strong>hello@kindro.co</strong><span>We reply within 24 hours</span></div>
</div>
<div class="abs info" style="top:1759px">
  <div class="ico"><svg width="14" height="14" viewBox="0 0 14 14"><path d="M3 1c1 0 2 2.5 2 3s-1.5 1-1.5 1.5c.5 2 2.5 4 4.5 4.5.5 0 1-1.5 1.5-1.5s3 1 3 2-1.5 2.5-2.5 2.5C5 13 1 9 1 3.5 1 2.5 2 1 3 1z" fill="#fff"/></svg></div>
  <div><strong>Have Any Qestion</strong><span>9170 2284</span></div>
</div>
<div class="abs info" style="top:1830px">
  <div class="ico"><svg width="14" height="14" viewBox="0 0 14 14"><circle cx="7" cy="7" r="6" fill="none" stroke="#fff"/><ellipse cx="7" cy="7" rx="2.6" ry="6" fill="none" stroke="#fff"/><path d="M1 7h12" stroke="#fff"/></svg></div>
  <div><strong>Website</strong><span>www.kindro.co</span></div>
</div>

<footer class="abs footer">
  <div class="brand"><span class="dot"></span>Kindro</div>
  <nav>
    <a style="left:370px">Home</a>
    <a style="left:454px">About us</a>
    <a style="left:554px">Our Solution</a>
    <a style="left:671px">Demonstration</a>
    <a style="left:803px">Contact Us</a>
  </nav>
  <span class="rule"></span>
  <span class="under"></span>
  <span class="fsoc" style="left:907px"></span>
  <span class="fsoc" style="left:946px"></span>
  <span class="fsoc" style="left:985px"></span>
  <span class="fsoc" style="left:1024px"></span>
  <p class="copy">@ Copyright  Aged care facilities 2018</p>
  <p class="back">Back Top <svg width="14" height="8" viewBox="0 0 14 8"><path d="M1 7l6-6 6 6" fill="none" stroke="#3d4b5e" stroke-width="1.3"/></svg></p>
</footer>

</body>
</html>
```